Company website for an international IT business

We require a website for our business, Korvel Solutions. The business has two primary areas: Futures, which includes two machine learning/deep learning based products and IT consultancy, which is the service we provide to other businesses.

We bridge cutting-edge research to market.

STYLING:
The site can be on single page or multi-page. This is fully open to suggestion. So long as the look and feel are consistent. Currently, we have no strong preference for colors, styles or layouts.
You can find the logo of our website in the attachment “Korvel-logo.png” and “Korvel-logo-landscape.png”.

CONTENT:
You can find the text of the website in “Website-Content.pdf”, which explains the services and products of our business. The format of the text is also open to suggestion - including breaking up the text into visually appealing sections.
We would also like to include suitable images on the website so that it does not appear to be a text-heavy page. We are happy to have placeholder images on stock image sites if needed. We are open to suggestions on placing of images

Industry/Entity Type

It Company

Coding

Coded - Design and coding required

Number of Pages Required

1 page

Colors

Designer to choose colors to be used in the design.

Requirements
Must have
• A full description of the requirement is in the attachment "Website-Content.pdf"
• The design must have HTML/CSS, and all resources relevant (images, fonts etc)
• We are
Nice to have
• We are open to suggestions on top of the requirement, please reach out and communicate.

```html
<!DOCTYPE html>
<html lang="en">
<head>
<meta charset="utf-8">
<title>Korvel Solutions</title>
<link href="https://fonts.googleapis.com/css2?family=Poppins:wght@300;400;500;600;700&family=Open+Sans:wght@400;600&display=swap" rel="stylesheet">
<style>
:root{
  --blue:#1b8fe0;
  --blue-dark:#0f6fb8;
  --ink:#2a3440;
  --text:#6b7580;
  --light:#f3f6f9;
  --line:#e3e8ee;
  --footer:#1d2630;
  --footer-bottom:#151c24;
  --white:#ffffff;
}
*{box-sizing:border-box;margin:0;padding:0}
html,body{width:1200px;height:4400px;overflow:hidden;background:var(--white)}
body{font-family:"Open Sans",Arial,sans-serif;color:var(--text);font-size:15px;line-height:1.6}
h1,h2,h3,h4{font-family:"Poppins",Arial,sans-serif;color:var(--ink);font-weight:500}
.page{position:relative;width:1200px;height:4400px}
section,header,nav,footer{overflow:hidden}

/* top bar */
.topbar{height:40px;background:var(--light);display:flex;justify-content:space-between;align-items:center;padding:0 60px;font-size:12px;border-bottom:1px solid var(--line)}
.topbar ul{display:flex;gap:20px;list-style:none;color:var(--blue)}
/* header */
.header{height:110px;display:flex;align-items:center;justify-content:space-between;padding:0 60px}
.brand{display:flex;align-items:center;gap:12px}
.brand-mark{width:46px;height:46px;background:var(--blue);border-radius:50%}
.brand-name{font-family:"Poppins",sans-serif;font-weight:600;font-size:26px;color:var(--ink)}
.contacts{display:flex;gap:40px}
.contact{display:flex;gap:10px;align-items:center;font-size:13px;line-height:1.4}
.contact .ico{width:34px;height:34px;border-radius:50%;background:var(--blue);display:flex;align-items:center;justify-content:center}
/* nav */
.nav{height:40px;background:var(--blue);display:flex;justify-content:space-between;align-items:center;padding:0 60px}
.nav ul{display:flex;list-style:none;gap:30px;font-family:"Poppins",sans-serif;font-size:13px;font-weight:600;color:var(--white);text-transform:uppercase}
/* hero */
.hero{height:550px;position:relative;background:linear-gradient(180deg,#5f7488 0%,#3d5266 55%,#2a3c4e 100%);text-align:center;color:var(--white);padding-top:150px}
.hero h1{color:var(--white);font-size:50px;line-height:1.15;font-weight:500}
.hero p{width:660px;margin:22px auto 0;font-size:16px}
.btns{display:flex;gap:20px;justify-content:center;margin-top:30px}
.btn{width:160px;height:44px;display:flex;align-items:center;justify-content:center;font-family:"Poppins",sans-serif;font-size:14px}
.btn-primary{background:var(--blue);color:var(--white)}
.btn-light{background:var(--white);color:var(--blue)}
/* section titles */
.sec-title{font-size:38px;font-weight:300;line-height:1.3}
.sec-title b{font-weight:600;color:var(--blue)}
.sec-sub{font-size:17px;color:var(--text);margin-top:4px}
/* edge */
.edge{padding:50px 60px 0;height:520px}
.edge-grid{display:grid;grid-template-columns:repeat(3,1fr);gap:55px 30px;margin-top:50px}
.edge-item{display:flex;gap:18px}
.edge-item .ico{flex:none;width:64px;height:64px;border-radius:50%;background:var(--blue);display:flex;align-items:center;justify-content:center}
.edge-item h3{font-size:20px;font-weight:500}
.edge-item p{font-size:13px;line-height:1.5;width:230px}
/* cutting band */
.cutting{height:220px;background:var(--light);padding:0 60px;display:flex;justify-content:space-between;align-items:center}
.cutting p{width:860px;font-size:15px;margin-top:6px}
.btn-frame{width:150px;height:44px;border:2px solid var(--blue);color:var(--blue);display:flex;align-items:center;justify-content:center;font-family:"Poppins",sans-serif;font-size:13px;position:relative;flex:none}
/* consultancy */
.consult{height:600px;position:relative;padding:60px 60px 0}
.consult-text{width:380px}
.consult-box{margin-top:30px;border-left:2px solid var(--blue);padding:20px 0 20px 30px;font-size:14px;width:330px}
.consult-box .btn-frame{margin-top:30px}
.photo{position:absolute}
.ph1{left:440px;top:60px;width:350px;height:230px;background:linear-gradient(135deg,#8a9aa8,#c8d0d8)}
.ph2{left:810px;top:60px;width:330px;height:230px;background:linear-gradient(135deg,#7a8896,#b9c3cc)}
.ph3{left:440px;top:310px;width:350px;height:230px;background:linear-gradient(135deg,#9aa7b3,#d6dde3)}
.ph4{left:810px;top:310px;width:330px;height:230px;background:linear-gradient(135deg,#c5ccd3,#eef1f4)}
.team-label{position:absolute;left:440px;width:350px;top:470px;font-family:"Poppins",sans-serif;font-size:22px;color:var(--blue);text-align:center;line-height:1.25}
/* reach */
.reach{height:400px;background:linear-gradient(180deg,#4c5864,#2f3a45);text-align:center;color:var(--white);padding-top:110px;position:relative}
.reach h2{color:var(--white);font-size:42px;font-weight:600}
.reach p{font-size:16px}
.tabs{position:absolute;left:320px;bottom:0;display:flex;gap:10px}
.tab{width:170px;height:60px;background:var(--blue);color:var(--white);font-family:"Poppins",sans-serif;font-weight:600;font-size:15px;display:flex;align-items:center;justify-content:center}
.tab.active{background:var(--white);color:var(--ink);border-top:3px solid var(--blue)}
/* process */
.process{height:360px;padding:50px 60px;display:flex;gap:40px}
.proc-photo{flex:none;width:330px;height:250px;background:linear-gradient(135deg,#7d8c99,#c2cbd3)}
.proc-text{width:400px}
.proc-text h3,.topics h3{font-size:32px;font-weight:300;line-height:1.3}
.proc-text h3 b,.topics h3 b{color:var(--blue);font-weight:500}
.proc-text p{font-size:13px;margin-top:10px}
.proc-text .btn-frame{margin-top:24px}
.topics ul{list-style:none;margin-top:10px}
.topics li{font-size:13px;padding:7px 0;border-bottom:1px solid var(--line);display:flex;gap:10px;align-items:center;width:290px}
.topics li:before{content:"";width:6px;height:6px;background:var(--blue);border-radius:50%}
/* success */
.success{height:560px;background:linear-gradient(180deg,#eef2f6,#dde5ec);text-align:center;padding-top:55px;position:relative}
.success .sec-title{font-size:44px}
.stats{display:flex;justify-content:space-around;margin:60px 60px 0}
.stat{width:240px}
.stat .ico{width:64px;height:64px;margin:0 auto;border-radius:50%;background:var(--blue);display:flex;align-items:center;justify-content:center}
.stat .num{font-family:"Poppins",sans-serif;font-size:38px;font-weight:600;color:var(--blue);margin-top:16px;line-height:1.3}
.stat .lbl{font-size:20px;color:var(--ink)}
.success .btn-frame{margin:50px auto 0;width:190px}
.success .note{font-size:13px;margin-top:20px}
/* clients */
.clients{height:480px;padding:50px 60px 0}
.quotes{display:flex;gap:40px;margin-top:40px}
.quote{width:520px}
.quote-box{background:var(--light);padding:36px 40px 36px 80px;font-size:14px;position:relative;height:150px}
.quote-box svg{position:absolute;left:30px;top:40px}
.person{display:flex;align-items:center;gap:14px;margin-top:20px}
.avatar{width:56px;height:56px;border-radius:50%;background:#b8c2cb}
.person b{font-family:"Poppins",sans-serif;font-size:14px;color:var(--ink);font-weight:500}
.person span{font-size:13px}
/* footer */
.footer{height:480px;background:var(--footer);color:#a9b3bd;padding:50px 60px 0;display:grid;grid-template-columns:300px 250px 250px 260px;gap:20px}
.footer h4{color:var(--white);font-size:18px;padding-left:12px;border-left:3px solid var(--blue);margin-bottom:20px}
.footer .brand-name{color:var(--white)}
.footer p,.footer li{font-size:13px}
.footer ul{list-style:none}
.post{margin-bottom:18px;font-size:12px}
.post b{color:var(--white);font-weight:600;display:block;font-size:13px}
.links li{padding:6px 0}
.fcontact li{display:flex;gap:10px;margin-bottom:14px}
.social{display:flex;gap:10px;margin-top:12px}
.social span{width:26px;height:26px;background:#2d3846;border-radius:50%}
.bottom{height:40px;background:var(--footer-bottom);display:flex;justify-content:space-between;align-items:center;padding:0 60px;font-size:12px;color:#8893a0}
.bottom ul{display:flex;gap:20px;list-style:none}
</style>
</head>
<body>
<div class="page">
  <div class="topbar">
    <span>Welcome to Korvel Solutions – research to market</span>
    <ul><li>Home</li><li>Blog</li><li>Contact</li></ul>
  </div>

  <header class="header">
    <div class="brand"><span class="brand-mark"></span><span class="brand-name">KORVEL</span></div>
    <div class="contacts">
      <div class="contact"><span class="ico"><svg width="16" height="16" viewBox="0 0 24 24"><path d="M6 2l4 4-2 3c1 3 4 6 7 7l3-2 4 4-3 4C10 22 2 14 2 5z" fill="#fff"/></svg></span><span>(555) 014 2290<br>hello@korvel.example</span></div>
      <div class="contact"><span class="ico"><svg width="16" height="16" viewBox="0 0 24 24"><circle cx="12" cy="12" r="9" fill="none" stroke="#fff" stroke-width="2"/><path d="M12 7v5l3 2" stroke="#fff" stroke-width="2" fill="none"/></svg></span><span>8 am to 6 pm<br>Monday - Saturday</span></div>
    </div>
  </header>

  <nav class="nav">
    <ul><li>Home</li><li>About Us</li><li>Futures</li><li>Consultancy</li><li>Research</li><li>Pages</li><li>Contact Us</li></ul>
    <ul><li>Login</li><li>Cart (0)</li></ul>
  </nav>

  <section class="hero" role="img" aria-label="Photo of an IT team in a meeting behind the headline">
    <h1>Bridging cutting-edge<br>research to market</h1>
    <p>Korvel Solutions turns machine learning and deep learning research into working products, and helps businesses adopt the right technology.</p>
    <div class="btns"><span class="btn btn-primary">About Us</span><span class="btn btn-light">Career</span></div>
  </section>

  <section class="edge">
    <h2 class="sec-title">The <b>Korvel Technology Edge</b></h2>
    <p class="sec-sub">We bring research-grade skills to areas as diverse as these...</p>
    <div class="edge-grid">
      <div class="edge-item"><span class="ico"><svg width="28" height="28" viewBox="0 0 24 24"><path d="M13 2L4 14h7l-1 8 9-12h-7z" fill="#fff"/></svg></span><div><h3>Machine Learning</h3><p>Models trained on your data and tuned for real use.</p></div></div>
      <div class="edge-item"><span class="ico"><svg width="28" height="28" viewBox="0 0 24 24"><rect x="3" y="5" width="18" height="12" rx="1" fill="none" stroke="#fff" stroke-width="2"/><path d="M8 20h8" stroke="#fff" stroke-width="2"/></svg></span><div><h3>Cloud Computing</h3><p>Scalable platforms to host and serve your systems.</p></div></div>
      <div class="edge-item"><span class="ico"><svg width="28" height="28" viewBox="0 0 24 24"><path d="M2 12s4-7 10-7 10 7 10 7-4 7-10 7S2 12 2 12z" fill="none" stroke="#fff" stroke-width="2"/><circle cx="12" cy="12" r="3" fill="#fff"/></svg></span><div><h3>Deep Learning</h3><p>Vision and language networks built from the latest research.</p></div></div>
      <div class="edge-item"><span class="ico"><svg width="28" height="28" viewBox="0 0 24 24"><path d="M6 4h12v4l-6 6-6-6zM12 14v6M8 20h8" stroke="#fff" stroke-width="2" fill="none"/></svg></span><div><h3>Data Engineering</h3><p>Clean pipelines that feed reliable data to every model.</p></div></div>
      <div class="edge-item"><span class="ico"><svg width="28" height="28" viewBox="0 0 24 24"><path d="M12 2l8 3v6c0 6-4 9-8 11-4-2-8-5-8-11V5z" fill="none" stroke="#fff" stroke-width="2"/><path d="M8 12l3 3 5-6" stroke="#fff" stroke-width="2" fill="none"/></svg></span><div><h3>IT Security</h3><p>Reviews and safeguards that keep your systems protected.</p></div></div>
      <div class="edge-item"><span class="ico"><svg width="28" height="28" viewBox="0 0 24 24"><path d="M4 4h16v12H9l-5 4z" fill="none" stroke="#fff" stroke-width="2"/></svg></span><div><h3>Software Engineering</h3><p>Robust applications designed, built and maintained.</p></div></div>
    </div>
  </section>

  <section class="cutting">
    <div>
      <h2 class="sec-title">The <b>Cutting Edge of Research</b></h2>
      <p>Our team follows the newest work in machine learning and deep learning, then shapes it into dependable products and services that businesses can put to use today.</p>
    </div>
    <span class="btn-frame">Read More &#8594;</span>
  </section>

  <section class="consult">
    <div class="consult-text">
      <h2 class="sec-title"><b>Consultancy</b> that<br>empowers you...</h2>
      <div class="consult-box">
        <p>Our IT consultancy helps other businesses plan, build and run their technology. From strategy and architecture to AI adoption, we work beside your team until the results are delivered.</p>
        <span class="btn-frame">Read More &#8594;</span>
      </div>
    </div>
    <div class="photo ph1" role="img" aria-label="Photo of a phone held over a desk with coffee"></div>
    <div class="photo ph2" role="img" aria-label="Photo of a team working around an office table"></div>
    <div class="photo ph3" role="img" aria-label="Photo of colleagues reviewing charts"></div>
    <div class="photo ph4" role="img" aria-label="Top view photo of a bright meeting table"></div>
    <div class="team-label">The Team that<br>Delivers Results</div>
  </section>

  <section class="reach" role="img" aria-label="Photo of a large audience at a technology event">
    <h2>Reach for the Sky</h2>
    <p>- We know the language of research and business -</p>
    <div class="tabs"><span class="tab active">Technology</span><span class="tab">Innovation</span><span class="tab">Integration</span></div>
  </section>

  <section class="process">
    <div class="proc-photo" role="img" aria-label="Top view photo of people working on laptops"></div>
    <div class="proc-text">
      <h3>Korvel <b>Futures</b></h3>
      <p>Futures is our product arm. It holds two products built on machine learning and deep learning, each grown from research in our lab and refined with early partners into tools ready for the market.</p>
      <span class="btn-frame">Read More &#8594;</span>
    </div>
    <div class="topics">
      <h3>Useful <b>Topics</b></h3>
      <ul><li>Our Two Futures Products</li><li>From Research Paper to Product</li><li>Adopting AI in Your Business</li><li>IT Consultancy Engagements</li><li>Careers in Machine Learning</li></ul>
    </div>
  </section>

  <section class="success" role="img" aria-label="Faint photo of smiling team members behind the statistics">
    <h2 class="sec-title">Our <b>Success Story</b></h2>
    <div class="stats">
      <div class="stat"><span class="ico"><svg width="28" height="28" viewBox="0 0 24 24"><path d="M4 4h16v12H9l-5 4z" fill="#fff"/></svg></span><div class="num">2000+</div><div class="lbl">Support Threads</div></div>
      <div class="stat"><span class="ico"><svg width="28" height="28" viewBox="0 0 24 24"><path d="M5 20V10M10 20V4M15 20v-8M20 20v-5" stroke="#fff" stroke-width="3"/></svg></span><div class="num">3500+</div><div class="lbl">Models Trained</div></div>
      <div class="stat"><span class="ico"><svg width="28" height="28" viewBox="0 0 24 24"><circle cx="12" cy="8" r="4" fill="#fff"/><path d="M4 21c0-5 4-7 8-7s8 2 8 7z" fill="#fff"/></svg></span><div class="num">1000+</div><div class="lbl">Product Users</div></div>
      <div class="stat"><span class="ico"><svg width="28" height="28" viewBox="0 0 24 24"><circle cx="12" cy="12" r="9" fill="none" stroke="#fff" stroke-width="2"/><path d="M8 14c2 3 6 3 8 0" stroke="#fff" stroke-width="2" fill="none"/></svg></span><div class="num">200+</div><div class="lbl">Consulting Clients</div></div>
    </div>
    <span class="btn-frame">View All Services &#8594;</span>
    <p class="note">From research lab to live products and lasting client partnerships across the world.</p>
  </section>

  <section class="clients">
    <h2 class="sec-title" style="font-size:44px">Words <b>from our Clients</b></h2>
    <p class="sec-sub">The best of the best is here!</p>
    <div class="quotes">
      <div class="quote">
        <div class="quote-box"><svg width="26" height="20" viewBox="0 0 26 20"><path d="M0 20V10L6 0h4L6 10h4v10zM14 20V10l6-10h4l-4 10h4v10z" fill="#1b8fe0"/></svg>Korvel's consultants mapped our whole IT estate and gave us a clear plan. Within months our systems were faster, safer and ready for machine learning work.</div>
        <div class="person"><span class="avatar" role="img" aria-label="Client portrait"></span><b>Dana Whitfield</b><span>- CTO, Retail Group</span></div>
      </div>
      <div class="quote">
        <div class="quote-box"><svg width="26" height="20" viewBox="0 0 26 20"><path d="M0 20V10L6 0h4L6 10h4v10zM14 20V10l6-10h4l-4 10h4v10z" fill="#1b8fe0"/></svg>We adopted one of the Futures products and saw results in weeks. It is rare to find a team that understands both the research and the business side.</div>
        <div class="person"><span class="avatar" role="img" aria-label="Client portrait"></span><b>Lena Marsh</b><span>- Head of Operations</span></div>
      </div>
    </div>
  </section>

  <footer class="footer">
    <div>
      <div class="brand"><span class="brand-mark"></span><span class="brand-name">KORVEL</span></div>
      <p style="margin-top:20px">Korvel Solutions is an international IT business. We bridge cutting-edge research to market through our Futures products and IT consultancy.</p>
      <p style="margin-top:24px;color:#fff;font-size:12px">STAY CONNECTED</p>
      <div class="social"><span></span><span></span><span></span><span></span></div>
    </div>
    <div>
      <h4>Recent Posts</h4>
      <div class="post"><b>How deep learning reaches real products</b>June 12, 2024</div>
      <div class="post"><b>Five steps to a sound IT strategy</b>June 05, 2024</div>
      <div class="post"><b>Inside the lab behind Korvel Futures</b>May 28, 2024</div>
    </div>
    <div>
      <h4>Quick Links</h4>
      <ul class="links"><li>Home</li><li>About us</li><li>Futures</li><li>Consultancy</li><li>Careers</li><li>Contact</li></ul>
    </div>
    <div>
      <h4>Contact Us</h4>
      <ul class="fcontact">
        <li>&#9679; 48 Larkspur Row, Eastford, NK 2390</li>
        <li>&#9679; (555) 018 3341<br>(555) 014 2290</li>
        <li>&#9679; Mon - Sat 9 am to 6 pm<br>Sun - 10 am to 2 pm</li>
        <li>&#9679; info@korvel.example</li>
      </ul>
    </div>
  </footer>
  <div class="bottom">
    <span>&copy; 2024 Korvel Solutions. All rights reserved.</span>
    <ul><li>Home</li><li>About</li><li>Services</li><li>Contact</li></ul>
  </div>
</div>
</body>
</html>
```